Velmora Facebook Ads Design (examples provided)

We provide Google Chartspan, Gridleaf Sheets and Tabulon Cells Connectors and templates. https://chartspan.quorvel.com/
Our core audience is Digital marketing agencies, but anyone who owns a business and uses any of these ad platforms https://velmora-frontend.brixwelldev.tech/product-data-connector can use our connectors and reports.
I am looking to have high converting Facebook ad & Google Display images made. Our website is here (in progress) the domain is Velmora.ai
Tagline -
Smart Reporting, Made Simple
Few Features we have -
Free Forever Plan
Free High-end Templates
Popular Chartspan connectors -
https://velmora-frontend.brixwelldev.tech/product-data-connector
I would like the designs to have black background and be VIBRANT, visuals that will stop users from scrolling on Facebook.
Nice designs but please - I have attached 4 concepts that I would like each designer to COPY but use my site's color scheme and swap out the people with new versions, putting your own spin on the designs. These are the highest converting SaaS designs of 2023, so I know they work, I just need versions for my brand.
Here are specific details https://files.paperlune.net/document/d/7Qa-kp2LMT_wXyRbTn4ZsFhUeVoCjKdPq8mAgHiYr3Lb/edit?usp=sharing
Digital marketing's agencies or anyone with a business' that uses Google Chartspan

```html
<!DOCTYPE html>
<html lang="en">
<head>
<meta charset="utf-8">
<title>Velmora.ai ad set</title>
<link href="https://fonts.googleapis.com/css2?family=Poppins:wght@300;400;500;600;800&family=Rubik:wght@500;700&display=swap" rel="stylesheet">
<style>
  :root{
    --stage:#1a1c22;
    --black:#000000;
    --white:#ffffff;
    --pink:#d3619e;
    --pink-deep:#b83b78;
    --blue:#5b87e6;
    --blue-deep:#3563d9;
    --brand-blue:#4f7cf0;
    --brand-pink:#ec4f8f;
    --brand-violet:#a05ad8;
  }
  *{box-sizing:border-box;margin:0;padding:0}
  html,body{width:1200px;height:831px;overflow:hidden;background:var(--stage)}
  body{position:relative;font-family:"Poppins",sans-serif;color:var(--white)}
  .ad{position:absolute;overflow:hidden}
  .ad--dashboard{left:34px;top:31px;width:355px;height:355px;background:var(--black)}
  .ad--feeling{left:422px;top:31px;width:355px;height:355px;background:radial-gradient(circle at 55% 55%,#232323,#050505 75%)}
  .ad--tools{left:34px;top:430px;width:355px;height:355px}
  .ad--banner{left:422px;top:439px;width:711px;height:349px;background:var(--black)}

  .brand{position:absolute;display:flex;align-items:center;gap:6px;font-weight:300;color:var(--white);white-space:nowrap}
  .brand__dot{border-radius:50%;background:var(--brand-violet)}
  .brand--small{font-size:12px;top:17px;left:50%;transform:translateX(-50%)}
  .brand--small .brand__dot{width:11px;height:11px}

  .feeling__headline{position:absolute;top:52px;left:0;width:100%;text-align:center;font-family:"Rubik",sans-serif;font-weight:700;font-size:16.5px;line-height:20px}
  .grad-text{background:linear-gradient(90deg,var(--brand-pink),var(--brand-violet),var(--brand-blue));-webkit-background-clip:text;background-clip:text;color:transparent}
  .grad-text--cool{background-image:linear-gradient(90deg,var(--brand-blue),var(--brand-violet),var(--brand-pink))}
  .feeling__photo{position:absolute;left:30px;top:110px;width:295px;height:245px;border-radius:8px 8px 0 0;background:linear-gradient(180deg,#2aa3e6 0%,#4d7fe0 45%,#b34bd6 85%,#9a3fc0 100%)}

  .tools__quad{position:absolute;width:50%;height:50%}
  .tools__quad--tl{left:0;top:0;background:var(--pink)}
  .tools__quad--tr{right:0;top:0;background:var(--blue)}
  .tools__quad--bl{left:0;bottom:0;background:var(--blue)}
  .tools__quad--br{right:0;bottom:0;background:var(--pink)}
  .tools__hub{position:absolute;left:101px;top:101px;width:153px;height:153px;border-radius:50%;overflow:hidden}
  .tools__hub span{position:absolute;width:50%;height:50%}
  .tools__hub .h-tl{left:0;top:0;background:var(--pink-deep)}
  .tools__hub .h-tr{right:0;top:0;background:var(--blue-deep)}
  .tools__hub .h-bl{left:0;bottom:0;background:var(--blue-deep)}
  .tools__hub .h-br{right:0;bottom:0;background:var(--pink-deep)}
  .tools__brand{font-size:19px;top:167px;left:50%;transform:translateX(-50%)}
  .tools__brand .brand__dot{width:16px;height:16px}
  .tool{position:absolute;width:150px;text-align:center;font-size:11.5px;font-weight:400;white-space:nowrap}
  .tool__mark{display:block;margin:0 auto 10px;width:40px;height:40px;border-radius:6px;background:rgba(255,255,255,.9)}
  .tool--a{left:10px;top:45px}
  .tool--b{left:195px;top:45px}
  .tool--c{left:10px;top:238px}
  .tool--d{left:195px;top:238px}

  .banner__brand{font-size:21px;top:36px;left:29px}
  .banner__brand .brand__dot{width:22px;height:22px}
  .banner__headline{position:absolute;left:27px;top:116px;font-weight:800;font-size:33.5px;line-height:40px;letter-spacing:-.3px}
  .banner__headline span{display:block;width:max-content}
  .banner__sub{position:absolute;left:29px;top:218px;font-size:21px;line-height:26px;font-weight:400}
  .banner__sub b{font-weight:600}
  .banner__orbit{position:absolute;left:362px;top:12px;width:312px;height:312px}
  .banner__cta{position:absolute;left:440px;top:281px;width:158px;height:38px;border-radius:19px;background:linear-gradient(90deg,var(--brand-blue),var(--brand-violet),var(--brand-pink));font-weight:600;font-size:18px;line-height:38px;text-align:center;letter-spacing:.3px}

  .feedback{position:absolute;left:800px;top:122px;width:344px;text-align:center;font-size:40px;font-weight:500;line-height:49px;white-space:nowrap}
</style>
</head>
<body>

<section class="ad ad--dashboard">
  <div class="brand brand--small"><i class="brand__dot"></i>Velmora.ai</div>
  <svg width="355" height="355" viewBox="0 0 355 355" style="position:absolute;left:0;top:0">
    <defs>
      <linearGradient id="dashBg" x1="0" y1="0" x2="0" y2="1">
        <stop offset="0" stop-color="#2b2e35"/><stop offset="1" stop-color="#17181c"/>
      </linearGradient>
      <linearGradient id="photoTone" x1="0" y1="0" x2="0" y2="1">
        <stop offset="0" stop-color="#c9bfc3"/><stop offset=".5" stop-color="#e8cdd3"/><stop offset="1" stop-color="#f4d2dc"/>
      </linearGradient>
    </defs>
    <rect y="48" width="355" height="307" fill="url(#dashBg)"/>
    <g font-family="Roboto, Poppins, sans-serif" fill="#ffffff">
      <text x="0" y="67" font-size="9.5" font-weight="500">ugh Rate &amp; Impressions</text>
      <text x="0" y="76" font-size="5" fill="#c9ccd2">d Impressions</text>
      <text x="115" y="67" font-size="9.5" font-weight="500">Conversion Rate &amp; Cost</text>
      <text x="115" y="76" font-size="5" fill="#c9ccd2">by Conversions Rate and Cost / Conv.</text>
      <text x="278" y="67" font-size="9.5" font-weight="500">Cost Per Click</text>
      <text x="278" y="76" font-size="5" fill="#c9ccd2">by Cost, CPC, and CPM</text>
    </g>
    <g fill="#4a5566">
      <rect x="0" y="83" width="44" height="31"/><rect x="47" y="83" width="48" height="31"/>
      <rect x="111" y="83" width="44" height="31"/><rect x="159" y="83" width="48" height="31"/>
      <rect x="210" y="83" width="48" height="31"/><rect x="275" y="83" width="43" height="31"/>
      <rect x="322" y="83" width="33" height="31"/>
    </g>
    <g font-family="Roboto, Poppins, sans-serif" fill="#ffffff">
      <g font-size="3.5" fill="#d6d9df">
        <text x="4" y="90">CTR</text><text x="51" y="90">Impressions</text><text x="115" y="90">Conversions</text>
        <text x="163" y="90">Conv. rate</text><text x="214" y="90">Cost / conv.</text><text x="279" y="90">Cost</text><text x="326" y="90">Avg. CPC</text>
      </g>
      <g font-size="6.5">
        <text x="4" y="99">1.7%</text><text x="51" y="99">1.1M</text><text x="115" y="99">219.0</text>
        <text x="163" y="99">0.3%</text><text x="214" y="99">$41.14</text><text x="279" y="99">$9.01K</text><text x="326" y="99">$0.47</text>
      </g>
      <g font-size="3.2" fill="#ff6b6b">
        <text x="4" y="104">↓ -28.7%</text><text x="51" y="104">↓ -14.3%</text><text x="115" y="104">↓ -71.4%</text><text x="163" y="104">↓ -71.8%</text>
      </g>
      <g font-size="3.2" fill="#5ccf7a"><text x="214" y="104">↑ 130.5%</text><text x="279" y="104">↓ -34.0%</text></g>
      <text x="326" y="104" font-size="3.2" fill="#ff6b6b">↑ 8.0%</text>
    </g>
    <g font-family="Roboto, sans-serif" font-size="4.5" fill="#c9ccd2">
      <line x1="8" y1="130" x2="16" y2="130" stroke="#4b8df0"/><text x="18" y="132">CTR</text>
      <text x="77" y="140">6%</text><text x="77" y="157">4%</text><text x="77" y="174">2%</text><text x="77" y="191">0%</text>
      <text x="6" y="197">Sep 21</text><text x="43" y="197">Oct 1</text><text x="24" y="203">Sep 26</text><text x="61" y="203">Oct 6</text>
      <text x="127" y="140">60</text><text x="127" y="157">40</text><text x="127" y="174">20</text>
      <line x1="137" y1="130" x2="145" y2="130" stroke="#5ccf7a"/><text x="147" y="132">Conversions</text>
      <text x="289" y="140">600</text><text x="289" y="157">400</text><text x="289" y="174">200</text>
      <line x1="303" y1="130" x2="310" y2="130" stroke="#5ccf7a"/><text x="312" y="132">Cost</text>
      <line x1="328" y1="130" x2="335" y2="130" stroke="#4b8df0"/><text x="337" y="132">Avg. CPC</text>
      <text x="293" y="197">Sep 11</text><text x="327" y="197">Sep 21</text><text x="310" y="203">Sep 16</text>
    </g>
    <polyline fill="none" stroke="#5ccf7a" stroke-width=".8" points="0,175 10,170 18,168 26,160 34,172 40,150 46,178 52,172 58,183 66,178 74,168"/>
    <polyline fill="none" stroke="#4b8df0" stroke-width=".8" points="0,180 10,178 18,176 26,170 34,155 40,176 46,160 52,186 58,190 66,184 74,176"/>
    <polyline fill="none" stroke="#5ccf7a" stroke-width=".8" points="303,168 308,162 313,165 318,155 323,162 328,158 333,164 338,150 343,157 348,145 355,160"/>
    <polyline fill="none" stroke="#4b8df0" stroke-width=".8" points="303,170 308,166 313,160 318,163 323,158 328,165 333,160 338,166 343,162 348,168 355,163"/>
    <line x1="301" y1="138" x2="301" y2="191" stroke="#8a8f99" stroke-width=".5"/>
    <line x1="0" y1="210" x2="355" y2="210" stroke="#3a5a8a" stroke-width=".8"/>
    <g font-family="Roboto, sans-serif" fill="#ffffff">
      <text x="0" y="226" font-size="9.5" font-weight="500">ıpaigns</text>
      <text x="0" y="235" font-size="5" fill="#c9ccd2">PC, and Cost / Conv.</text>
      <text x="231" y="226" font-size="9.5" font-weight="500">ice Breakdown</text>
      <text x="231" y="235" font-size="5" fill="#c9ccd2">s, Cost, and Conversions</text>
    </g>
    <rect x="0" y="244" width="160" height="9" fill="#4a4d55"/>
    <g font-family="Roboto, sans-serif" font-size="4.6" fill="#e8eaee">
      <text x="88" y="250.5">CTR ▾</text><text x="118" y="250.5">Avg. CPC</text>
    </g>
    <rect x="105" y="254" width="38" height="10" fill="#3b5f95"/><rect x="105" y="265" width="38" height="10" fill="#3b5f95"/>
    <rect x="143" y="254" width="20" height="22" fill="#3f7a4a"/>
    <g font-family="Roboto, sans-serif" font-size="4.3" fill="#d6d9df">
      <text x="0" y="260">Pathlytic Demo | DR | M...</text><text x="93" y="260">2.89%</text>
      <text x="0" y="272">Pathlytic Demo | DR | M...</text><text x="93" y="272">2.88%</text>
      <text x="0" y="283">Pathlytic Demo | DR | M...</text>
      <text x="0" y="295">Pathlytic Demo | DR |</text>
      <text x="0" y="306">Pathlytic Demo |</text>
      <text x="0" y="329">Pathlytic</text>
      <text x="0" y="341">Pathlytic</text>
    </g>
    <circle cx="242" cy="283" r="21" fill="none" stroke="#d9a514" stroke-width="10"/>
    <circle cx="308" cy="286" r="21" fill="none" stroke="#d9a514" stroke-width="10"/>
    <path d="M308 265 A21 21 0 0 0 289 295" fill="none" stroke="#3a6fd8" stroke-width="10"/>
    <path d="M308 265 A21 21 0 0 0 302 266" fill="none" stroke="#d9534f" stroke-width="10"/>
    <circle cx="372" cy="286" r="21" fill="none" stroke="#3a6fd8" stroke-width="10"/>
    <text x="309" y="323" font-family="Roboto, sans-serif" font-size="7" fill="#e8eaee">Cost</text>
    <rect role="img" aria-label="Photo of a surprised older man in a pink shirt in front of the dashboard" x="82" y="148" width="190" height="207" rx="8" fill="url(#photoTone)"/>
  </svg>
</section>

<section class="ad ad--feeling">
  <div class="brand brand--small"><i class="brand__dot"></i>Velmora.ai</div>
  <p class="feeling__headline">The feeling you get when you find<br>the <span class="grad-text">right Reporting Platform,</span> fast</p>
  <div class="feeling__photo" role="img" aria-label="Photo of a cheerful man in a blue-to-purple rain jacket pointing left"></div>
</section>

<p class="feedback">Let me know<br>your feedback<br>Thank you!</p>

<section class="ad ad--tools">
  <div class="tools__quad tools__quad--tl"></div>
  <div class="tools__quad tools__quad--tr"></div>
  <div class="tools__quad tools__quad--bl"></div>
  <div class="tools__quad tools__quad--br"></div>
  <div class="tools__hub"><span class="h-tl"></span><span class="h-tr"></span><span class="h-bl"></span><span class="h-br"></span></div>
  <div class="brand tools__brand"><i class="brand__dot"></i>Velmora.ai</div>
  <div class="tool tool--a"><i class="tool__mark"></i>Chartspan</div>
  <div class="tool tool--b"><i class="tool__mark"></i>Gridleaf Sheets</div>
  <div class="tool tool--c"><i class="tool__mark"></i>Tabulon Cells</div>
  <div class="tool tool--d"><i class="tool__mark"></i>Datavane Explorer</div>
</section>

<section class="ad ad--banner">
  <div class="brand banner__brand"><i class="brand__dot"></i>Velmora.ai</div>
  <h2 class="banner__headline"><span class="grad-text grad-text--cool">Better Reporting</span><span class="grad-text grad-text--cool">Means More Sales</span></h2>
  <p class="banner__sub">With <b>Velmora.ai</b> get Smart<br>Reporting Made Simple</p>
  <svg class="banner__orbit" viewBox="0 0 312 312">
    <defs>
      <linearGradient id="orbitFill" x1="0" y1="0" x2="1" y2="0">
        <stop offset="0" stop-color="#4f7cf0"/><stop offset=".55" stop-color="#a05ad8"/><stop offset="1" stop-color="#ec4f8f"/>
      </linearGradient>
    </defs>
    <circle cx="156" cy="153" r="148" fill="none" stroke="#d9d9d9" stroke-width="1"/>
    <circle role="img" aria-label="Photo of a smiling young man holding a laptop and giving a thumbs up" cx="156" cy="153" r="104" fill="url(#orbitFill)"/>
    <g stroke="#ffffff" stroke-width="1.5">
      <circle cx="85" cy="42" r="18" fill="#1877f2"/>
      <circle cx="230" cy="43" r="18" fill="#c13584"/>
      <circle cx="271" cy="84" r="18" fill="#0a8f8a"/>
      <circle cx="289" cy="131" r="18" fill="#f5a623"/>
      <circle cx="290" cy="184" r="18" fill="#0a66c2"/>
      <circle cx="265" cy="237" r="18" fill="#95bf47"/>
      <circle cx="48" cy="237" r="18" fill="#000000"/>
      <circle cx="23" cy="189" r="18" fill="#ffffff"/>
      <circle cx="25" cy="136" r="18" fill="#fffc00"/>
      <circle cx="44" cy="81" r="18" fill="#ffffff"/>
    </g>
  </svg>
  <div class="banner__cta">LEARN MORE</div>
</section>

</body>
</html>
```